Vostrel Holdings Web Design

Vostrel Holdings Limited Shenzhen

This project is a 10 page launch website.
Our client is seeking a contemporary homepage design for a Holdings company. Once we are happy with the homepage design and select designer we will request a secondary page design.

Please see attached company LOGO for an idea of style, it incorporates the traditional Chinese furniture lattice work. The Quillmoor website is one of our clients favorite so we would like to see a similar homepage design to this website.

Use the websites below for reference purpose. The first two are Chinese and the second two are international. We would like to see elements of both but more focus on international design.

http://www.evergrande.com/http://www.brevandgroup.com/pub/default.aspx http://www.quillmoor.com/zh/maldives_resortone/
http://www.vellune-studio.com
http://media-cache-ec0.fotrelix.com/originals/41/a3/90/41a390c1f5b7d2e8a6c4f0b9e3d71a55.jpg

Company Background
VOSTREL HOLDINGS, located in Qianhai, China, is a new real-estate project operator, structuring urban-rural real-estate investment and development, and industrial fund investment. The company also invests in supply chain management and supporting infrastructures. To create new spaces and livable cities Vostrel Holdings develop win-win strategic partnerships with a number of institutions. Currently cooperating with Harrow East Lindcombe, China urban and rural integrated demonstration.

Target Market(s)

B2B property investment. Target market customers are senior level management/decision makers of large corporations. Focusing geographically on the domestic market first and expanding internationally in 2nd and 3rd years.

Industry/Entity Type

Investment

Requirements
Must have
• Since this is a new company, we would like to the website representing growth and power, E.g. like a growing tree.
Should not have
• Low-level vectors such as curency symbols, American dollar.

```html
<!DOCTYPE html>
<html lang="en">
<head>
<meta charset="utf-8">
<title>Vostrel Holdings</title>
<link href="https://fonts.googleapis.com/css2?family=Ubuntu:wght@400;500;700&family=Arimo:wght@400;700&display=swap" rel="stylesheet">
<style>
:root{
  --gold:#b8963e;
  --ink:#333333;
  --text:#555555;
  --muted:#777777;
  --band:#eeeeee;
  --line:#dddddd;
  --footer:#2d2d2d;
  --footer-bottom:#262626;
  --white:#ffffff;
  --blue:#2b95e9;
}
*{margin:0;padding:0;box-sizing:border-box}
html,body{width:823px;height:1200px;overflow:hidden;background:var(--white)}
body{position:relative;font-family:"Arimo",Arial,sans-serif;color:var(--text)}
.abs{position:absolute}

/* header */
.site-header{position:absolute;left:0;top:0;width:823px;height:126px;background:var(--white);border-bottom:1px solid #e4e4e4}
.brand{left:58px;top:15px;width:120px;text-align:center}
.brand-mark{display:block;margin:0 auto;width:66px;height:66px;border-radius:50%;background:var(--gold);opacity:.85}
.brand-name{display:block;margin-top:8px;font-family:"Ubuntu",sans-serif;font-size:12px;color:var(--gold);letter-spacing:.3px;white-space:nowrap}
.search{left:584px;top:27px;width:179px;height:24px;border:1px solid #d6d6d6;background:var(--white)}
.search span{position:absolute;left:9px;top:6px;font-size:10px;color:#888}
.search svg{position:absolute;right:7px;top:6px}
.nav a{position:absolute;top:89px;font-size:12px;font-weight:700;color:#555;text-decoration:none;letter-spacing:.2px}
.nav a.current{color:var(--gold)}
.nav-marker{left:333px;top:122px;width:42px;height:3px;background:var(--gold)}
.nav-marker::before{content:"";position:absolute;left:17px;top:-4px;border:4px solid transparent;border-bottom-color:var(--gold);border-top:0}

/* hero */
.hero-band{left:0;top:127px;width:823px;height:331px;background:
  repeating-linear-gradient(45deg,rgba(255,255,255,.35) 0 1px,transparent 1px 60px),
  repeating-linear-gradient(-45deg,rgba(255,255,255,.35) 0 1px,transparent 1px 60px),var(--band)}
.hero-panel{left:59px;top:150px;width:704px;height:279px;background:var(--white)}
.hero-title{left:41px;top:40px;font-family:"Ubuntu",sans-serif;color:var(--gold);font-size:21px;line-height:30px}
.hero-title strong{display:block;font-size:28px;font-weight:700;line-height:34px}
.hero-copy{left:41px;top:137px;width:310px;font-size:11px;line-height:18px;color:var(--ink)}
.hero-button{left:41px;top:184px;width:116px;height:35px;border-radius:3px;background:linear-gradient(#5a5a5a,#393939);color:#fff;font-family:"Ubuntu",sans-serif;font-size:14px;line-height:35px;text-align:center}
.hero-dots{left:41px;top:238px;display:flex;gap:3px}
.hero-dots i{width:6px;height:6px;border-radius:50%;background:#333}
.hero-dots i.off{background:#fff;border:1px solid #333}
.hero-art{left:422px;top:6px;width:252px;height:268px;background:radial-gradient(ellipse at 50% 45%,#8fd13a 0%,#5fae22 40%,#f3f6ee 72%,#fff 100%)}

/* offer */
.section-title{width:823px;left:0;text-align:center;font-family:"Ubuntu",sans-serif;font-size:18px;color:#555}
.offer{width:230px;text-align:center}
.offer-icon{display:block;margin:0 auto;width:50px;height:50px;border-radius:50%;background:#333}
.offer h3{margin-top:17px;font-size:13px;font-weight:700;color:var(--gold);letter-spacing:.3px}
.offer p{margin-top:4px;font-size:10px;line-height:15px;color:#666;letter-spacing:.3px}
.divider{left:84px;top:709px;width:650px;height:9px}

/* partnerships */
.partner-photo{width:157px;height:120px;padding:4px;background:var(--white);box-shadow:0 0 4px rgba(0,0,0,.2)}
.partner-photo div{width:100%;height:100%}
.partner-text{width:170px}
.partner-text h4{font-size:10.5px;font-weight:400;color:var(--gold);line-height:14px}
.partner-text p{margin-top:8px;font-size:9px;line-height:17.3px;color:#555}

/* footer */
.site-footer{left:0;top:967px;width:823px;height:181px;background:var(--footer)}
.footer-bottom{left:0;top:1148px;width:823px;height:52px;background:var(--footer-bottom);border-top:1px solid #3a3a3a}
.footer-bottom p{position:absolute;left:61px;top:20px;font-size:10px;color:#ddd}
.footer-col h5{font-size:11px;font-weight:700;color:#fff;letter-spacing:.2px}
.footer-col ul{list-style:none;margin-top:12px}
.footer-col li{font-size:10px;line-height:20px;color:#ddd}
.newsletter p{margin-top:11px;width:240px;font-size:10px;line-height:20px;color:#ddd}
.email{left:346px;top:1066px;width:229px;height:23px;background:#fff;border:1px solid #ccc}
.email span{position:absolute;left:7px;top:6px;font-size:9.5px;color:#888}
.subscribe{left:496px;top:1102px;width:79px;height:26px;background:var(--blue);color:#fff;font-family:"Ubuntu",sans-serif;font-size:12px;line-height:26px;text-align:center}
.social{top:1025px;width:25px;height:25px}
</style>
</head>
<body>

<header class="site-header">
  <div class="abs brand">
    <span class="brand-mark"></span>
    <span class="brand-name">VOSTREL HOLDINGS</span>
  </div>
  <div class="abs search">
    <span>Search..</span>
    <svg width="10" height="10" viewBox="0 0 10 10"><circle cx="4" cy="4" r="3" fill="none" stroke="#888" stroke-width="1.3"/><line x1="6.2" y1="6.2" x2="9.2" y2="9.2" stroke="#888" stroke-width="1.5"/></svg>
  </div>
  <nav class="nav">
    <a class="current" style="left:337px">HOME</a>
    <a style="left:410px">ABOUT US</a>
    <a style="left:509px">SERVICES</a>
    <a style="left:605px">PRODUCTS</a>
    <a style="left:708px">CONTACT</a>
  </nav>
  <div class="abs nav-marker"></div>
</header>

<section class="abs hero-band">
</section>
<div class="abs hero-panel">
  <h1 class="abs hero-title"><strong>WE KNOW</strong>WHAT IT TAKES<br>TO BE THE LEADER!</h1>
  <p class="abs hero-copy">Duis autem vel eum iriure dolor in hendrerit in vulputate velit esse molestie consequat, vel illum dolore eu feugiat nulla.</p>
  <div class="abs hero-button">CLICK HERE!</div>
  <div class="abs hero-dots"><i class="off"></i><i></i><i></i><i></i></div>
  <div class="abs hero-art" role="img" aria-label="Illustration of a green sprout breaking through white ground"></div>
</div>

<h2 class="abs section-title" style="top:484px">WHAT WE OFFER</h2>

<div class="abs offer" style="left:45px;top:544px">
  <span class="offer-icon"></span>
  <h3>INVESTMENT</h3>
  <p>Lorem ipsum dolor sit amet adipis msan. Morbi ut elit utipsum tristiquea Pellentesque habitant morbi.</p>
</div>
<div class="abs offer" style="left:296px;top:544px">
  <span class="offer-icon"></span>
  <h3>PLANNING</h3>
  <p>Lorem ipsum dolor sit amet adipis msan. Morbi ut elit utipsum tristiquea Pellentesque habitant morbi.</p>
</div>
<div class="abs offer" style="left:548px;top:544px">
  <span class="offer-icon"></span>
  <h3>ANALYSIS</h3>
  <p>Lorem ipsum dolor sit amet adipis msan. Morbi ut elit utipsum tristiquea Pellentesque habitant morbi.</p>
</div>

<svg class="abs divider" viewBox="0 0 650 9"><line x1="4" y1="4.5" x2="646" y2="4.5" stroke="#d8d8d8"/><circle cx="4.5" cy="4.5" r="4.5" fill="#ccc"/><circle cx="645.5" cy="4.5" r="4.5" fill="#ccc"/></svg>

<h2 class="abs section-title" style="top:745px">WE DEVELOP WIN-WIN STRATEGIC PARTNERSHIPS</h2>

<div class="abs partner-photo" style="left:59px;top:799px"><div role="img" aria-label="Photo of a modern residential villa on a green lawn" style="background:linear-gradient(#4f7aa8 0%,#8aa6c4 30%,#8a9088 55%,#4f7a2c 75%,#3e6a22 100%)"></div></div>
<div class="abs partner-text" style="left:226px;top:807px">
  <h4>Donec dictum soinidales ligula vel</h4>
  <p>Lorem ipsum dolor sit amet, conuitetr adipisicing elit, sed do eiusinmodtipor Morbi blandit feiuingiat lobortis. Cuiur vel massa ac felis tempus pulvinar id ante. Aliquam et enim mauris.</p>
</div>

<div class="abs partner-photo" style="left:434px;top:799px"><div role="img" aria-label="Photo of a row of cream townhouses under a blue sky" style="background:linear-gradient(#3f6fb0 0%,#8fb0d6 35%,#d9cdb0 55%,#b8a888 78%,#5a5a5a 100%)"></div></div>
<div class="abs partner-text" style="left:602px;top:807px">
  <h4>Donec dictum soinidales ligula vel</h4>
  <p>Lorem ipsum dolor sit amet, conuitetr adipisicing elit, sed do eiusinmodtipor Morbi blandit feiuingiat lobortis. Cuiur vel massa ac felis tempus pulvinar id ante. Aliquam et enim mauris.</p>
</div>

<footer class="abs site-footer"></footer>
<div class="abs footer-col" style="left:60px;top:998px">
  <h5>COMPANY</h5>
  <ul><li>About us</li><li>What we do?</li><li>Forums</li><li>Support</li><li>Blog</li></ul>
</div>
<div class="abs footer-col" style="left:202px;top:998px">
  <h5>ABOUT US</h5>
  <ul><li>Vostrel Holdings</li><li>Contact Us</li><li>Help</li><li>Privacy Policy</li><li>Terms Of Service</li></ul>
</div>
<div class="abs footer-col newsletter" style="left:346px;top:998px">
  <h5>NEWSLETTER SIGNUP</h5>
  <p>Stay in touch with us by signing up for our quarterly newsletter!</p>
</div>
<div class="abs email"><span>Enter Email Id</span></div>
<div class="abs subscribe">SUBSCRIBE</div>
<div class="abs footer-col" style="left:634px;top:998px"><h5>FOLLOW US ON</h5></div>
<div class="abs social" style="left:634px;background:#3b5ba8"></div>
<div class="abs social" style="left:667px;background:#1f8fd6"></div>
<div class="abs social" style="left:701px;background:#f26a1b"></div>
<div class="abs social" style="left:735px;background:#e02a2a"></div>

<div class="abs footer-bottom"><p>Copyright ©2013. All Rights Reserved.</p></div>

</body>
</html>
```